Tallgrove Vale Management

I need a professional website. My current website is tallgrovevalemanagement.com and I hate it. It was created with some AI tool very quickly because I needed a site up and running with no advanced notice. I’m open to all designs .. I trust you, the professionals will deliver the results I’m anxiously awaiting! :)

```html
<!DOCTYPE html>
<html lang="en">
<head>
<meta charset="utf-8">
<title>Tallgrove Vale Management</title>
<link href="https://fonts.googleapis.com/css2?family=Montserrat:wght@700;800;900&family=Inter:wght@400;500;600;700&display=swap" rel="stylesheet">
<style>
:root{
  --navy:#1e2a44;
  --navy-deep:#1b2640;
  --red:#c4262e;
  --ink:#3c4458;
  --muted:#5b6272;
  --paper:#ffffff;
  --mist:#f5f6f8;
  --band-gray:#5d6166;
  --faded:#6e7890;
}
*{box-sizing:border-box;margin:0;padding:0}
html,body{width:1200px;height:2301px;overflow:hidden;background:var(--paper)}
body{position:relative;font-family:"Inter",sans-serif;color:var(--ink)}
.display{font-family:"Montserrat",sans-serif;font-weight:900;text-transform:uppercase;color:var(--navy);letter-spacing:-0.02em}
.red{color:var(--red)}
.eyebrow{position:absolute;display:flex;align-items:center;gap:12px;font-family:"Montserrat",sans-serif;font-weight:800;font-size:8.5px;letter-spacing:.02em;text-transform:uppercase;color:var(--ink);white-space:nowrap}
.eyebrow::before{content:"";width:19px;height:2px;background:var(--red)}
.eyebrow.wide{letter-spacing:.18em;font-size:9px;gap:14px}
.eyebrow.wide::before{width:30px}
.btn{position:absolute;display:flex;align-items:center;justify-content:center;gap:10px;font-family:"Inter",sans-serif;font-weight:700;font-size:9px;letter-spacing:.12em;text-transform:uppercase;border:1.5px solid var(--navy);white-space:nowrap}
.btn.solid{background:var(--red);color:#fff;border-color:var(--red);box-shadow:3px 3px 0 var(--navy)}
.btn.line{background:#fff;color:var(--navy);box-shadow:3px 3px 0 var(--navy)}

/* nav */
.site-nav{position:absolute;left:0;top:0;width:1200px;height:71px;background:#fff}
.nav-link{position:absolute;top:30px;font-size:9px;font-weight:500;letter-spacing:.14em;color:var(--ink);white-space:nowrap}
.brand{position:absolute;left:536px;top:28px;width:130px;display:flex;align-items:center;justify-content:center;gap:5px;font-family:"Montserrat",sans-serif;font-weight:800;font-size:11px;color:var(--navy);text-transform:uppercase;letter-spacing:.01em;white-space:nowrap}
.brand-mark{width:8px;height:8px;background:var(--red);flex:none}

/* hero */
.hero{position:absolute;left:0;top:71px;width:1200px;height:529px;background:#f2f3f5;overflow:hidden}
.hero-photo{position:absolute;left:0;top:0;width:1200px;height:529px;background:linear-gradient(115deg,#c9ccd1 0%,#dcdee2 35%,#eceef0 60%,#f2f3f5 70%);clip-path:polygon(0 0,740px 0,800px 250px,660px 529px,0 529px)}
.hero-rule{position:absolute;left:0;top:600px;width:1200px;height:5px;background:var(--navy)}
.hero-title{position:absolute;left:196px;top:75px;font-size:61px;line-height:64px;white-space:nowrap}
.hero-underline{position:absolute;left:196px;top:328px;width:566px;height:4px;background:#c4c7cd}
.hero-lead{position:absolute;left:196px;top:350px;width:420px;padding-left:17px;border-left:2px solid var(--navy);font-size:13px;line-height:20.5px;color:var(--muted)}

/* services */
.services{position:absolute;left:0;top:605px;width:1200px;height:603px;background:#fafafb}
.services-shade{position:absolute;left:800px;top:0;width:400px;height:603px;background:#f3f4f6;clip-path:polygon(40px 0,400px 0,400px 603px,0 603px)}
.section-title{position:absolute;font-size:29px;line-height:37px}
.card{position:absolute;background:#fff;border:1px solid var(--navy);box-shadow:3px 3px 0 var(--navy)}
.card-icon{position:absolute;width:41px;height:41px;border:1.5px solid var(--navy);box-shadow:2px 2px 0 var(--navy);background:#fff;display:flex;align-items:center;justify-content:center}
.card h3{position:absolute;font-family:"Montserrat",sans-serif;font-weight:900;font-size:11.5px;color:var(--navy);text-transform:uppercase;letter-spacing:-0.01em}
.card p{position:absolute;font-size:10px;line-height:16.5px;color:var(--muted)}

.band-gray{position:absolute;left:0;top:1208px;width:1200px;height:4px;background:var(--band-gray)}

/* strategy */
.strategy{position:absolute;left:0;top:1212px;width:1200px;height:462px;background:var(--mist)}
.strategy-card{position:absolute;left:217px;top:54px;width:438px;height:341px;background:#fff;border:1.5px solid var(--navy);box-shadow:5px 5px 0 var(--navy)}
.strategy-title{position:absolute;left:31px;top:53px;font-size:22px;line-height:29px;width:390px}
.strategy-lead{position:absolute;left:31px;top:129px;width:380px;padding-left:16px;border-left:2px solid var(--red);font-size:11.3px;line-height:18.5px;color:var(--muted)}
.strategy-rule{position:absolute;left:31px;top:241px;width:376px;height:1px;background:var(--navy)}
.stat{position:absolute;top:253px}
.stat b{display:block;font-family:"Montserrat",sans-serif;font-weight:900;font-size:30px;color:var(--navy);letter-spacing:-0.01em}
.stat b.red{color:var(--red)}
.stat span{display:block;margin-top:2px;font-size:7.5px;font-weight:600;letter-spacing:.2em;color:var(--ink)}
.pillar{position:absolute;left:676px;width:307px;height:100px;background:var(--navy);box-shadow:3px 3px 0 var(--red);padding:23px 21px}
.pillar h4{font-family:"Montserrat",sans-serif;font-weight:900;font-size:12px;color:#fff;text-transform:uppercase;letter-spacing:-0.01em}
.pillar p{margin-top:6px;font-size:8.3px;line-height:12.5px;color:#d9dde5}

.band-navy{position:absolute;left:0;top:1674px;width:1200px;height:5px;background:var(--navy)}

/* contact */
.cta{position:absolute;left:217px;top:1730px;width:771px;height:432px;border:1.5px solid var(--navy);box-shadow:4px 4px 0 var(--navy);background:#fff}
.cta-panel{position:absolute;left:305px;top:-1.5px;width:467px;height:433px;background:var(--navy-deep);text-align:center}
.cta-eyebrow{position:absolute;left:0;top:142px;width:467px;font-family:"Montserrat",sans-serif;font-weight:800;font-size:8px;color:var(--red);text-transform:uppercase}
.cta-panel-title{position:absolute;left:0;top:168px;width:467px;font-size:22px;line-height:28px;color:#fff}
.cta-title{position:absolute;left:41px;top:64px;font-size:21px;line-height:28.5px}
.cta-lead{position:absolute;left:41px;top:196px;width:215px;padding-left:16px;border-left:2px solid var(--red);font-size:9.8px;line-height:16.5px;color:var(--muted)}
.contact-box{position:absolute;left:41px;top:293px;width:224px;height:93px;border:1.5px solid var(--navy);box-shadow:3px 3px 0 var(--navy);padding:26px 22px}
.contact-item{display:flex;align-items:center;gap:10px;font-family:"Montserrat",sans-serif;font-weight:800;font-size:8.5px;color:var(--navy);text-transform:uppercase;height:14px;margin-bottom:21px}

/* footer */
.band-foot{position:absolute;left:0;top:2210px;width:1200px;height:4px;background:var(--band-gray)}
.site-footer{position:absolute;left:0;top:2214px;width:1200px;height:87px;background:var(--navy)}
.foot-brand{position:absolute;left:200px;top:36px;display:flex;align-items:center;gap:5px;font-family:"Montserrat",sans-serif;font-weight:800;font-size:8px;color:#fff;text-transform:uppercase}
.foot-brand span{width:6px;height:6px;background:var(--red)}
.foot-divider{position:absolute;left:262px;top:30px;width:1px;height:22px;background:#3a4660}
.foot-text{position:absolute;font-size:7.5px;font-weight:600;letter-spacing:.12em;line-height:10px;text-transform:uppercase;color:#c9cedb}
</style>
</head>
<body>

<header class="site-nav">
  <span class="nav-link" style="left:362px">SERVICES</span>
  <span class="nav-link" style="left:430px">WHY TALLGROVE</span>
  <div class="brand"><span class="brand-mark"></span>Tallgrove Vale</div>
  <span class="nav-link" style="left:676px">CONTACT</span>
  <div class="btn solid" style="left:739px;top:18px;width:148px;height:35px">Request Proposal</div>
</header>

<section class="hero">
  <div class="hero-photo" role="img" aria-label="Upward view of glass office towers, washed in pale gray"></div>
  <div class="eyebrow wide" style="left:196px;top:52px">Cleveland &amp; Akron Property Management</div>
  <h1 class="display hero-title">Expertise<br>Rooted in<br><span class="red">Asset<br>Preservation.</span></h1>
  <div class="hero-underline"></div>
  <p class="hero-lead">A true partner, not just a vendor. We protect, manage, and grow your real estate investments by applying rigorously tested frameworks and data-driven methodologies.</p>
  <div class="btn solid" style="left:196px;top:444px;width:233px;height:36px">Request a Tailored Proposal
    <svg width="11" height="9" viewBox="0 0 11 9"><path d="M0 4.5h9M5.5 1l3.5 3.5L5.5 8" fill="none" stroke="#fff" stroke-width="1.4"/></svg></div>
  <div class="btn line" style="left:444px;top:444px;width:168px;height:36px">Explore Our Services</div>
</section>
<div class="hero-rule"></div>

<section class="services">
  <div class="services-shade"></div>
  <div class="eyebrow" style="left:217px;top:56px">Management Solutions</div>
  <h2 class="display section-title" style="left:217px;top:80px">Comprehensive<br><span class="red">Optimization</span></h2>
  <div class="btn line" style="left:832px;top:117px;width:151px;height:36px">View All Packages</div>

  <article class="card" style="left:217px;top:193px;width:505px;height:162px">
    <div class="card-icon" style="left:231px;top:20px">
      <svg width="22" height="22" viewBox="0 0 22 22" fill="none" stroke="#c4262e" stroke-width="1.5"><circle cx="8" cy="7" r="4"/><path d="M1 19c0-4 3-6 7-6s7 2 7 6"/><path d="M14 9l2 2 4-4"/></svg>
    </div>
    <h3 style="left:20px;top:83px">Tenant Placement &amp; Screening</h3>
    <p style="left:20px;top:109px;width:450px">Finding the right tenant is the foundation of asset preservation. We utilize comprehensive, rigorous screening processes to ensure reliable, high-quality placements.</p>
  </article>

  <article class="card" style="left:217px;top:374px;width:505px;height:162px">
    <div class="card-icon" style="left:231px;top:20px">
      <svg width="22" height="22" viewBox="0 0 22 22" fill="none" stroke="#c4262e" stroke-width="1.5"><path d="M2 2v18h18"/><path d="M6 14l4-5 3 3 5-6"/></svg>
    </div>
    <h3 style="left:20px;top:83px">Financial Optimization &amp; Reporting</h3>
    <p style="left:20px;top:109px;width:470px">Gain complete transparency through our data-driven financial methodologies. Access real-time statements, performance metrics, and profitability tracking through our dedicated owner portal.</p>
  </article>

  <article class="card" style="left:741px;top:193px;width:242px;height:343px">
    <div class="card-icon" style="left:100px;top:86px">
      <svg width="22" height="22" viewBox="0 0 22 22" fill="none" stroke="#c4262e" stroke-width="1.5"><path d="M11 2l8 3v6c0 5-4 8-8 9-4-1-8-4-8-9V5z"/><path d="M7.5 11l2.5 2.5 4.5-4.5"/></svg>
    </div>
    <h3 style="left:0;width:240px;text-align:center;top:149px">Proactive Maintenance</h3>
    <p style="left:22px;width:196px;text-align:center;top:174px">Protect your investment with our 24/7 preventative and responsive maintenance frameworks. We preserve your property's condition while keeping your tenants highly satisfied.</p>
  </article>
</section>
<div class="band-gray"></div>

<section class="strategy">
  <div class="strategy-card">
    <div class="eyebrow" style="left:31px;top:34px">Our Strategy</div>
    <h2 class="display strategy-title">Your Strategic Real Estate Partner</h2>
    <p class="strategy-lead">Rooted in the Cleveland-Akron market, our team leverages deep local insights and corporate-level operational frameworks to protect your assets. Whether scaling a portfolio or seeking peace of mind for a single investment, we provide consultative, transparent, and results-oriented management.</p>
    <div class="strategy-rule"></div>
    <div class="stat" style="left:31px"><b>98%</b><span>OCCUPANCY RATE</span></div>
    <div class="stat" style="left:142px"><b class="red">24/7</b><span>RESPONSE FRAMEWORK</span></div>
  </div>
  <div class="pillar" style="top:54px"><h4>Radical Transparency</h4><p>Real-time data, clear financial statements, and honest communication.</p></div>
  <div class="pillar" style="top:175px"><h4>Asset Preservation</h4><p>Preventative maintenance today saves thousands in capital expenditures tomorrow.</p></div>
  <div class="pillar" style="top:295px"><h4>Tenant Retention</h4><p>We foster respectful, responsive relationships with tenants to ensure occupancy.</p></div>
</section>
<div class="band-navy"></div>

<section class="cta">
  <div class="eyebrow" style="left:41px;top:42px">Partner With Us</div>
  <h2 class="display cta-title">Ready to<br>Elevate Your<br>Property's<br>Performance?</h2>
  <p class="cta-lead">Submit the form to initiate a consultative assessment. We will explore bespoke solutions perfectly aligned with your unique investment objectives.</p>
  <div class="contact-box">
    <div class="contact-item"><svg width="14" height="11" viewBox="0 0 14 11" fill="none" stroke="#c4262e" stroke-width="1.3"><rect x="1" y="1" width="12" height="9" rx="1"/><path d="M1 2l6 4.5L13 2"/></svg>Email Us</div>
    <div class="contact-item"><svg width="14" height="14" viewBox="0 0 14 14" fill="none" stroke="#c4262e" stroke-width="1.3"><path d="M7 13s5-4.5 5-8A5 5 0 0 0 2 5c0 3.5 5 8 5 8z"/><circle cx="7" cy="5" r="1.8"/></svg>Service Area</div>
  </div>
  <div class="cta-panel">
    <div class="cta-eyebrow">Initiate Assessment</div>
    <h2 class="display cta-panel-title">Request a Tailored<br>Proposal</h2>
    <div class="btn solid" style="left:88px;top:251px;width:283px;height:36px;box-shadow:none">Begin Assessment
      <svg width="11" height="9" viewBox="0 0 11 9"><path d="M0 4.5h9M5.5 1l3.5 3.5L5.5 8" fill="none" stroke="#fff" stroke-width="1.4"/></svg></div>
  </div>
</section>

<div class="band-foot"></div>
<footer class="site-footer">
  <div class="foot-brand"><span></span>Tallgrove</div>
  <div class="foot-divider"></div>
  <div class="foot-text" style="left:282px;top:36px">© 2026. All rights<br>reserved.</div>
  <div class="foot-text" style="left:442px;top:36px;color:var(--faded)">Proudly serving Greater Cleveland &amp; Akron,<br>Ohio</div>
  <div class="foot-text" style="left:712px;top:36px">Privacy</div>
  <div class="foot-text" style="left:771px;top:36px">Terms</div>
  <div class="foot-text" style="left:821px;top:36px;color:#fff">Owner<br>Portal</div>
  <div class="foot-text" style="left:911px;top:36px;color:#fff">Tenant<br>Portal</div>
</footer>

</body>
</html>
```